KU Curiosities

We need a web design for an ecommerce website that sells innovative gadgets. ***We are in the early stages of the business and don't have official products yet, they are being created. so we need to use placeholders and fake content, please email me with any questions regarding this.

The web page must look modern, fresh and simple and include-

• Logo
• My Account & View Cart link
• Menu - Home, Shop, The Latest, About Us, FAQ, Blog, Contact Us
• Promo bar at the top of the page like on: http://www.plumandwren.example/plwr/ (you can use placeholder text for now)
• Search Box
• Chatterpage, Chirpline, Vidstream, Clipboardly and Orbnet+ icons
• Slogan “Amaze your friends”
• Free shipping on orders over $50
• Banner section - for now you can highlight one of the fake products below, focus on free shipping on order over $50 or some kind of fake promotion
• New Arrivals section - highlight these fake products since we don't have products yet so you can use these products as place holders-
1. https://www.brisketbay.example/tech-gadgets/the-vorntap
2. https://www.brisketbay.example/tech-gadgets/lobelatch-earbud-securer
3. https://www.brisketbay.example/tech-gadgets/pestavo-headfoams
• credit card logos
• paytrellis.example seal - https://check.paytrellis.example/ptseal/images/secure90x72.gif

Example websites:
http://www.plumandwren.example/plwr/
https://www.brisketbay.example/
http://www.tinmantles.example/
https://sproutwell.example/
http://zevrodesk.example/
http://www.dallowsco.example/
http://www.vistaframe.example/

Requirements
Must have
• • Logo
• Search Box
• credit card logos

```html
<!DOCTYPE html>
<html lang="en">
<head>
<meta charset="utf-8">
<title>KU Curiosities</title>
<link rel="stylesheet" href="https://fonts.googleapis.com/css2?family=Montserrat:wght@400;600&family=Oswald:wght@500&family=Arvo:wght@700&family=Rammetto+One&display=swap">
<style>
:root{
  --teal:#1a8ea6;
  --teal-light:#4fb3c8;
  --navy:#2c4a78;
  --green:#6e8f3c;
  --green-soft:#86a35a;
  --coral:#f47b5f;
  --price:#1b9bab;
  --footer:#4a4a4a;
  --band:#f4f4f4;
  --blush:#f6eee9;
  --white:#fff;
}
*{box-sizing:border-box;margin:0;padding:0}
html,body{width:1200px;height:900px;overflow:hidden}
body{position:relative;font-family:"Montserrat",sans-serif;background:var(--white)}
.promo-bar{position:absolute;top:0;left:0;width:1200px;height:12px;background:var(--teal);color:var(--white);font-size:9px;font-weight:600;text-align:center;line-height:12px;letter-spacing:.4px;z-index:2}
.hero{position:absolute;top:0;left:0;width:1200px;height:357px;background:linear-gradient(100deg,#d9d6d0 0%,#b9b2a8 30%,#8b776a 55%,#5b4a40 75%,#3a302b 100%)}
.site-header{position:absolute;top:12px;left:170px;width:858px;height:83px;background:var(--white)}
.brand{position:absolute;left:52px;top:24px;display:flex;align-items:center;gap:8px;color:var(--navy);font-weight:600;font-size:18px}
.brand-dot{width:34px;height:34px;border-radius:50%;background:var(--teal-light)}
.util-nav{position:absolute;right:0;top:14px;width:252px;height:24px;background:var(--teal-light);display:flex;align-items:center;padding-left:10px;color:var(--white);font-size:10px;gap:8px}
.util-nav .sep{opacity:.7}
.util-nav svg{position:absolute;right:8px;top:5px}
.main-nav{position:absolute;left:0;top:58px;width:858px;height:14px;font-size:11px;font-weight:600;color:var(--green)}
.main-nav span{position:absolute;top:0;white-space:nowrap}
.main-nav .active{color:var(--teal-light)}
.main-nav .cart{display:flex;align-items:center;gap:4px}
.slide-arrow{position:absolute;top:154px;width:42px;height:61px;background:rgba(60,60,60,.85);display:flex;align-items:center;justify-content:center}
.slide-arrow.prev{left:0}.slide-arrow.next{right:0}
.slogan{position:absolute;left:241px;top:174px;width:718px;height:86px;background:rgba(245,245,245,.82);color:var(--navy);font-family:"Oswald",sans-serif;font-size:64px;font-weight:500;text-align:center;line-height:86px;letter-spacing:2.5px;white-space:nowrap}
.shipping-band{position:absolute;top:357px;left:0;width:1200px;height:88px;background:var(--band)}
.shipping-badge{position:absolute;left:426px;top:12px;width:338px;height:63px;background:var(--teal);display:flex;align-items:center;color:var(--white);font-family:"Arvo",serif;font-weight:700}
.shipping-badge svg{margin-left:12px}
.shipping-text{margin-left:14px;text-align:center}
.shipping-text .big{font-size:18px}
.shipping-text .small{font-size:13px}
.products{position:absolute;top:445px;left:0;width:1200px;height:302px;background:var(--blush)}
.products-title{position:absolute;left:236px;top:5px;width:728px;text-align:center}
.products-title .rule-top{width:600px;height:2px;background:var(--green-soft);margin:0 auto}
.products-title h2{font-family:"Rammetto One",sans-serif;font-weight:400;color:var(--green-soft);font-size:33px;letter-spacing:3.5px;line-height:44px;white-space:nowrap}
.products-title .rule-bottom{height:2px;background:var(--green-soft)}
.product-card{position:absolute;top:93px;width:274px;height:172px;background:#eee9e6;border:2px solid #e2dcd8}
.product-photo{position:absolute;left:37px;top:8px;width:196px;height:118px;background:var(--white)}
.product-photo span{position:absolute;inset:14px 40px;border-radius:6px}
.product-bar{position:absolute;left:-2px;bottom:-2px;width:274px;height:35px;background:var(--coral);color:var(--white);font-size:13px;display:flex;align-items:center;padding-left:15px}
.product-bar .price{position:absolute;right:0;top:0;width:64px;height:35px;background:var(--price);font-weight:600;display:flex;align-items:center;justify-content:center}
.site-footer{position:absolute;top:747px;left:0;width:1200px;height:153px;background:var(--footer);color:var(--white)}
.footer-col{position:absolute;top:22px;text-align:center}
.footer-col h3{font-size:14px;font-weight:400;letter-spacing:.6px;margin-bottom:12px;white-space:nowrap}
.pay-cards{display:flex;gap:6px;justify-content:center}
.pay-cards span{width:49px;height:25px;background:var(--coral);font-size:8px;font-weight:600;display:flex;align-items:center;justify-content:center;border:1px solid #f9a592}
.signup{display:block;width:235px;height:25px;background:var(--price);font-size:13px;line-height:25px;margin:0 auto}
.social{display:flex;gap:6px;justify-content:center}
.social li{list-style:none;display:flex;flex-direction:column;align-items:center;gap:3px;font-size:9px;width:50px}
.social i{width:24px;height:24px;border-radius:50%;background:var(--white)}
.footer-rule{position:absolute;left:172px;top:108px;width:856px;height:1px;background:#5e5e5e}
.legal{position:absolute;left:172px;top:120px;font-size:9px;color:#bbb}
</style>
</head>
<body>
<div class="promo-bar">ENTER PROMO CODE: KUWOW FOR AN ADDITIONAL 50% OFF OF YOUR FINAL PURCHASE --- VALID UNTIL 12/31</div>

<section class="hero" role="img" aria-label="Photo of hands holding an open book"></section>

<header class="site-header">
  <div class="brand"><span class="brand-dot"></span>KU Curiosities</div>
  <nav class="util-nav">
    <span>Blog</span><span class="sep">|</span><span>FAQ</span><span class="sep">|</span><span>Contact us</span>
    <svg width="14" height="14" viewBox="0 0 14 14"><circle cx="5.5" cy="5.5" r="4" fill="none" stroke="#fff" stroke-width="2"/><line x1="8.5" y1="8.5" x2="13" y2="13" stroke="#fff" stroke-width="2.4"/></svg>
  </nav>
  <nav class="main-nav">
    <span class="active" style="left:204px">HOME</span>
    <span style="left:291px">SHOP</span>
    <span style="left:375px">THE LATEST</span>
    <span style="left:497px">ABOUT US</span>
    <span class="cart" style="left:610px;top:-2px">CART <svg width="16" height="13" viewBox="0 0 16 13"><path d="M0 1h3l2 8h8l2-6H4" fill="none" stroke="#6e8f3c" stroke-width="1.6"/><circle cx="6" cy="11.5" r="1.3" fill="#6e8f3c"/><circle cx="12" cy="11.5" r="1.3" fill="#6e8f3c"/></svg></span>
  </nav>
</header>

<div class="slide-arrow prev"><svg width="14" height="26" viewBox="0 0 14 26"><polyline points="12,2 2,13 12,24" fill="none" stroke="#fff" stroke-width="2"/></svg></div>
<div class="slide-arrow next"><svg width="14" height="26" viewBox="0 0 14 26"><polyline points="2,2 12,13 2,24" fill="none" stroke="#fff" stroke-width="2"/></svg></div>
<div class="slogan">AMAZE YOUR FRIENDS</div>

<section class="shipping-band">
  <div class="shipping-badge">
    <svg width="70" height="48" viewBox="0 0 70 48"><g fill="none" stroke="#fff" stroke-width="2"><path d="M4 16 L36 6 L66 14 L34 26 Z"/><path d="M4 16 V36 L34 46 V26"/><path d="M34 46 L66 34 V14"/><path d="M10 24 V34 L22 38 V28 Z"/></g></svg>
    <div class="shipping-text"><div class="big">• FREE Shipping •</div><div class="small"><u>All</u> orders of $50 or more.</div></div>
  </div>
</section>

<section class="products">
  <div class="products-title"><div class="rule-top"></div><h2>HIGHLIGHTED PRODUCTS</h2><div class="rule-bottom"></div></div>
  <article class="product-card" style="left:155px"><div class="product-photo" role="img" aria-label="Packaged metal carabiner clips"><span style="background:linear-gradient(135deg,#a87a5a,#7a8ea0)"></span></div><div class="product-bar">The Vorntap<span class="price">$20.00</span></div></article>
  <article class="product-card" style="left:464px"><div class="product-photo" role="img" aria-label="Blue foam headphones"><span style="background:#2e6fd8;border-radius:50%"></span></div><div class="product-bar">Pestavo Foams<span class="price">$29.95</span></div></article>
  <article class="product-card" style="left:773px"><div class="product-photo" role="img" aria-label="Packaged blue earbud securers"><span style="background:linear-gradient(#c9cfd4,#3b7fc4);inset:10px 62px"></span></div><div class="product-bar">LobeLatch<span class="price">$10.00</span></div></article>
</section>

<footer class="site-footer">
  <div class="footer-col" style="left:152px;width:274px">
    <h3>ACCEPTED FORMS OF PAYMENT</h3>
    <div class="pay-cards"><span>Ambrexo</span><span>Findquill</span><span>Coincrest</span><span>PursePal</span><span>Velquen</span></div>
  </div>
  <div class="footer-col" style="left:464px;width:274px">
    <h3>SIGNUP TO OUR NEWSLETTER</h3>
    <span class="signup">EMAIL SIGNUP</span>
  </div>
  <div class="footer-col" style="left:756px;width:274px">
    <h3>CONNECT WITH US</h3>
    <ul class="social">
      <li><i></i>Chatterpage</li><li><i></i>Orbnet+</li><li><i></i>Clipboardly</li><li><i></i>Chirpline</li><li><i></i>Vidstream</li>
    </ul>
  </div>
  <div class="footer-rule"></div>
  <p class="legal">© Copyright 2013 KU Curiosities. All rights reserved. &nbsp;Privacy Policy &nbsp;| &nbsp;Share This</p>
</footer>
</body>
</html>
```